Social Media Marketing website

Need website designed for social media marketing company BrightLoop.com
Do no currently have logo.
Pages:
Main
Services
Order
Contact
Please use dummy text for now. I will provide content to winner later to add.
Main page should clearly show the steps with some sort of graphic: Establish, Engage, Analyze.
Services provided (steps):
1) Establish social media presence
2) Social media management and advertising
3) Analyze and engage
Site should be simple, clean and attractive. Design examples:
http://plinkster.com/
http://www.quillbase.com/
http://www.harrowvalemq.com/
Be creative! It should not look like a template.
Updates
Updated examples.
Contact me for questions.
dave@brightloop.com
3) Analyze and engage
Advertising

```html
<!DOCTYPE html>
<html lang="en">
<head>
<meta charset="utf-8">
<title>BrightLoop – Social Media Marketing</title>
<link href="https://fonts.googleapis.com/css2?family=Questrial&family=Noto+Sans:wght@400;700&display=swap" rel="stylesheet">
<style>
:root{
  --page-bg:#a39b91;
  --panel:#ffffff;
  --brand:#8e1521;
  --brand-dark:#6e0c16;
  --ink:#222222;
  --muted:#555555;
  --nav-bg:#efefef;
  --soft:#f2f2f2;
  --line:#d6d6d6;
  --base:#857a67;
  --base-dark:#5f5649;
  --head-font:"Questrial",sans-serif;
  --body-font:"Noto Sans",Verdana,sans-serif;
}
*{box-sizing:border-box;margin:0;padding:0}
html,body{width:1048px;height:1200px;overflow:hidden}
body{background:var(--page-bg);font-family:var(--body-font);color:var(--ink);position:relative}
.abs{position:absolute}

.base{left:115px;top:830px;width:817px;height:306px;background:var(--base);border-radius:0 0 22px 22px}
.footer-band{left:115px;top:1094px;width:817px;height:42px;background:var(--base-dark);border-radius:0 0 22px 22px}
.footer-links,.copyright{top:1111px;font-size:8.5px;color:#f1ece4;letter-spacing:.4px}
.footer-links{left:135px}
.footer-links span{margin:0 6px}
.copyright{right:136px}

.sheet{left:114px;top:58px;width:819px;height:804px;background:var(--panel);border-radius:22px}

.brand-mark{left:136px;top:82px;width:68px;height:68px;border-radius:50%;background:var(--brand)}
.tagline{left:207px;top:88px;font-family:var(--head-font);font-size:12px;color:var(--ink)}
.brand-name{left:205px;top:96px;font-family:var(--head-font);font-size:52px;color:var(--brand);line-height:1}

.find-us{left:692px;top:97px;font-family:var(--head-font);font-size:16px;color:var(--ink)}
.social{left:782px;top:92px;display:flex;gap:4px}
.social i{display:block;width:27px;height:27px;border-radius:4px}
.call{left:698px;top:130px;font-family:var(--head-font);font-size:16px;color:var(--ink)}
.call b{font-family:var(--body-font);font-size:20px;color:var(--brand);margin-left:3px}

.nav{left:135px;top:171px;width:778px;height:42px;background:var(--nav-bg);border-radius:22px 22px 0 0}
.nav-home{left:135px;top:171px;width:96px;height:40px;background:var(--brand);border-radius:20px 10px 0 0;color:#fff;font-weight:700;font-size:12px;display:flex;align-items:center;justify-content:center;padding-top:4px}
.nav-item{top:186px;font-family:var(--head-font);font-size:13px;color:var(--ink)}
.search{left:756px;top:179px;width:140px;height:20px;background:#fff;border:1px solid var(--line);font-size:10px;color:#999;padding:3px 5px}
.search svg{position:absolute;right:4px;top:3px}

.hero{left:136px;top:208px;width:777px;height:305px;border:1.5px solid var(--brand);border-radius:20px 0 0 20px;background:linear-gradient(90deg,#fafafa,#ececec 40%);overflow:hidden}
.hero-photo{left:262px;top:0;width:514px;height:304px;background:radial-gradient(circle at 50% 45%,#f6eee6 0,#d9b79c 40%,#8c6a55 70%,#e9e3d6 100%)}
.hero-title{left:145px;top:248px;font-family:var(--body-font);font-weight:700;font-style:italic;font-size:20px;color:var(--brand)}
.hero-copy{left:146px;top:284px;width:234px;font-size:10.4px;line-height:11.7px;color:var(--ink)}
.hero-copy p+p{margin-top:11.7px}
.btn{background:var(--brand);color:#fff;font-size:11px;display:flex;align-items:center;justify-content:center}
.hero-btn{left:306px;top:477px;width:76px;height:24px;font-weight:700}
.dots{left:845px;top:215px;display:flex;gap:3px}
.dots i{display:block;width:11px;height:11px;border-radius:50%;border:1.5px solid var(--brand);background:#fff}
.dots i:first-child{background:var(--brand)}

.step-title{top:541px;font-family:var(--head-font);font-size:16px;line-height:20px;color:var(--ink)}
.divider{top:537px;width:2px;height:298px;background:#ececec}
.step-art{top:585px;width:194px;height:98px;border:1px solid var(--line)}
.step-text{width:205px;font-size:9.4px;line-height:11.7px;color:var(--ink)}
.step-more{font-size:9.8px;font-weight:700;color:var(--brand);letter-spacing:.5px}

.box{background:var(--soft);border:1px solid #e5e5e5;border-radius:3px}
.testimonials{left:136px;top:870px;width:342px;height:214px;background:#fff}
.card{left:144px;width:327px;height:84px;background:linear-gradient(#fff,#f0f0f0);border:1px solid #e4e4e4;border-radius:3px}
.avatar{width:68px;height:69px;background:linear-gradient(#f2e7df,#b98e73)}
.card-text{left:229px;width:233px;font-size:9.4px;line-height:11.7px;color:var(--ink)}
.scroll-tab{left:280px;width:45px;height:22px;background:#d8d8d8;border-radius:50%}

.about{left:485px;top:870px;width:426px;height:214px;background:linear-gradient(#fff,#f1f1f1)}
.section-title{font-family:var(--head-font);font-size:16.5px;color:var(--ink)}
.about-item{left:496px;width:190px;font-size:9.4px;line-height:11.7px;color:var(--ink)}
.about-divider{left:689px;top:876px;width:1px;height:202px;background:#e2e2e2}
.field{left:707px;width:189px;background:#ececec;border:1px solid #d5d5d5;font-size:10px;color:#777;padding:6px 7px}
.small-btn{height:20px;font-size:11px}
</style>
</head>
<body>

<div class="abs base"></div>
<div class="abs footer-band"></div>
<div class="abs footer-links">Site map<span>|</span>Services<span>|</span>Order<span>|</span>Contac us</div>
<div class="abs copyright">Copyright @ 2011 BrightLoop</div>

<div class="abs sheet"></div>

<header>
  <div class="abs brand-mark"></div>
  <div class="abs tagline">OFFER SOCIAL SOLUTIONS</div>
  <div class="abs brand-name">BrightLoop</div>

  <div class="abs find-us">Find us on:</div>
  <div class="abs social" aria-label="Social profiles">
    <i style="background:#6bb7e0"></i><i style="background:#e8672a"></i><i style="background:#3b5c9c"></i><i style="background:#c8c8c8"></i>
  </div>
  <div class="abs call">Call Now: <b>222-608-3190</b></div>
</header>

<nav>
  <div class="abs nav"></div>
  <div class="abs nav-home">HOME</div>
  <div class="abs nav-item" style="left:244px">SERVICES</div>
  <div class="abs nav-item" style="left:320px">|</div>
  <div class="abs nav-item" style="left:349px">ORDER</div>
  <div class="abs nav-item" style="left:413px">|</div>
  <div class="abs nav-item" style="left:441px">CONTACT US</div>
  <div class="abs search">Search here...
    <svg width="13" height="13" viewBox="0 0 13 13"><circle cx="5" cy="5" r="3.6" fill="none" stroke="#333" stroke-width="1.5"/><path d="M7.7 7.7 12 12" stroke="#333" stroke-width="2"/></svg>
  </div>
</nav>

<section class="abs hero">
  <div class="abs hero-photo" role="img" aria-label="Photo of smiling young people in a circle looking down at the camera"></div>
</section>
<h1 class="abs hero-title">BRIGHT LOOP</h1>
<div class="abs hero-copy">
  <p>Lorem Ipsum is simply dummy text of the printing and typesetting industry. Lorem Ipsum has been the industry's standard dummy text ever since the 1500s, when an unknown printer took a galley of type and scrambled it to make a type specimen book. It has survived not only five centuries, but also the leap into electronic typesetting, remaining essentially unchanged.</p>
  <p>It was popularised in the 1960s with the release of Vantaro sheets containing Lorem Ipsum passages, and more recently with desktop publishing software like Quillset PageForge including versions of Lorem Ipsum.</p>
</div>
<div class="abs btn hero-btn">Read more</div>
<div class="abs dots"><i></i><i></i><i></i><i></i></div>

<section class="steps">
  <h2 class="abs step-title" style="left:161px">Establish social media<br>presence</h2>
  <h2 class="abs step-title" style="left:416px">Social media management<br>and advertising</h2>
  <h2 class="abs step-title" style="left:681px">Analyze and engage</h2>
  <div class="abs divider" style="left:384px"></div>
  <div class="abs divider" style="left:645px"></div>

  <div class="abs step-art" style="left:161px;background:linear-gradient(135deg,#f4f4f4,#d4d4d4)" role="img" aria-label="Collage of social media word clippings"></div>
  <div class="abs step-art" style="left:414px;background:linear-gradient(180deg,#c9c9c9,#8a8a8a 60%,#2a2a2a)" role="img" aria-label="Stack of newspapers on a keyboard"></div>
  <div class="abs step-art" style="left:677px;background:radial-gradient(circle at 55% 35%,#3a8fd6 0,#3a8fd6 22%,#c4a27a 45%,#f5f5f5 75%)" role="img" aria-label="Cardboard box filled with blue figure icons"></div>

  <p class="abs step-text" style="left:161px;top:693px">Lorem Ipsum is simply dummy text of the printing and typesetting..</p>
  <p class="abs step-more" style="left:295px;top:724px">Read more..</p>
  <p class="abs step-text" style="left:161px;top:747px">Lorem Ipsum is simply dummy text of the printing and typesetting..</p>
  <p class="abs step-more" style="left:295px;top:777px">Read more..</p>
  <p class="abs step-text" style="left:161px;top:800px">Lorem Ipsum is simply dummy text of the printing and typesetting..</p>
  <p class="abs step-more" style="left:295px;top:830px">Read more..</p>

  <p class="abs step-text" style="left:412px;top:693px">Lorem Ipsum is simply dummy text of the printing and typesetting..</p>
  <p class="abs step-more" style="left:546px;top:724px">Read more..</p>
  <p class="abs step-text" style="left:412px;top:747px">Lorem Ipsum is simply dummy text of the printing and typesetting..</p>
  <p class="abs step-more" style="left:546px;top:777px">Read more..</p>
  <p class="abs step-text" style="left:412px;top:800px">Lorem Ipsum is simply dummy text of the printing and typesetting..</p>
  <p class="abs step-more" style="left:546px;top:830px">Read more..</p>

  <p class="abs step-text" style="left:680px;top:693px">Lorem Ipsum is simply dummy text of the printing and typesetting..</p>
  <p class="abs step-more" style="left:814px;top:724px">Read more..</p>
  <p class="abs step-text" style="left:680px;top:747px">Lorem Ipsum is simply dummy text of the printing and typesetting..</p>
  <p class="abs step-more" style="left:814px;top:777px">Read more..</p>
  <p class="abs step-text" style="left:680px;top:800px">Lorem Ipsum is simply dummy text of the printing and typesetting..</p>
  <p class="abs step-more" style="left:814px;top:830px">Read more..</p>
</section>

<section class="testimonials-area">
  <div class="abs box testimonials"></div>
  <div class="abs scroll-tab" style="top:859px"></div>
  <svg class="abs" style="left:295px;top:864px" width="14" height="9" viewBox="0 0 14 9"><path d="M2 7 7 2l5 5" fill="none" stroke="#222" stroke-width="2.4"/></svg>

  <div class="abs card" style="top:889px"></div>
  <div class="abs avatar" style="left:152px;top:897px" role="img" aria-label="Portrait photo of a client"></div>
  <p class="abs card-text" style="top:907px">Lorem Ipsum is simply dummy text of the print-ing and typesetting industry. Lorem Ipsum has been the industry's standard..</p>
  <p class="abs step-more" style="left:400px;top:949px">Read more</p>

  <div class="abs card" style="top:979px"></div>
  <div class="abs avatar" style="left:152px;top:987px" role="img" aria-label="Portrait photo of a client"></div>
  <p class="abs card-text" style="top:997px">Lorem Ipsum is simply dummy text of the print-ing and typesetting industry. Lorem Ipsum has been the industry's standard..</p>
  <p class="abs step-more" style="left:400px;top:1039px">Read more</p>

  <div class="abs scroll-tab" style="top:1068px"></div>
  <svg class="abs" style="left:295px;top:1072px" width="14" height="9" viewBox="0 0 14 9"><path d="M2 2l5 5 5-5" fill="none" stroke="#222" stroke-width="2.4"/></svg>
</section>

<section>
  <div class="abs box about"></div>
  <h3 class="abs section-title" style="left:496px;top:884px">Read More About us</h3>
  <p class="abs about-item" style="top:920px">Lorem Ipsum is simply dummy text of the printing and typesetting.</p>
  <p class="abs about-item" style="top:952px">Lorem Ipsum is simply dummy text of the printing and typesetting.</p>
  <p class="abs about-item" style="top:983px">Lorem Ipsum is simply dummy text of the printing and typesetting.</p>
  <p class="abs about-item" style="top:1015px">Lorem Ipsum is simply dummy text of the printing and typesetting.</p>
  <div class="abs btn small-btn" style="left:613px;top:1058px;width:63px">Continue</div>
  <div class="abs about-divider"></div>

  <h3 class="abs section-title" style="left:707px;top:884px">Contact Us</h3>
  <div class="abs field" style="top:911px;height:25px">Name</div>
  <div class="abs field" style="top:944px;height:25px">E-mail</div>
  <div class="abs field" style="top:977px;height:74px">Message</div>
  <div class="abs btn small-btn" style="left:831px;top:1058px;width:63px">Submit</div>
</section>

</body>
</html>
```